Business Card Design - Construction Company

Torvane Construction is in need of a sharp, modern business card design that has an architectural/high fashion feel.

We are looking for a two sided card.

One side simple dark grey/black with some texture in the background. e.g. (a mosaic of simple interconnecting shapes or a shadow of the logo.) Something to draw attention and create interest.It will need to feature a large Torvane construction logo (files attached) in metallic gradient or plain white.

The other side should contain all of our information:

(in largest text)
Name of person
Torvane Construction Pty. Ltd.

Licensed builders specialising in:
- Bathrooms
- Kitchens
- Commercial interiors

(mid sized text)
Phone number
Fax number
person@torvaneconstruction.example.au
www. torvaneconstruction.example.au

(smaller text)
ABN: 47209836512
BSA license: xxx-xxxx
PO Box 8640 Dunmore QLD 4170 (address)

Target Market(s)

professional home and business owners

Industry/Entity Type

Construction

Requirements
Must have
• Must be bold, professional looking and modern.
Nice to have
• We are undecided as to what kind of printing we will go with.
Definitely square edged.
Probably high quality satin card.
We are also interested in designs that would work well on transparent or translucent plastic.
Ideally we would print two versions.
Should not have
• Nothing with an antique feel.
No wild colours. Small amounts of colour can be good in the right place.

```html
<!DOCTYPE html>
<html lang="en">
<head>
<meta charset="utf-8">
<title>Torvane Construction – Business Card</title>
<link rel="stylesheet" href="https://fonts.googleapis.com/css2?family=Saira:wght@400;500;600&display=swap">
<style>
  :root {
    --page-bg: #d9d6d0;
    --card-black: #0d0d0e;
    --card-shade: #1c1c1e;
    --text-white: #f2f2f2;
    --silver: #e4e4e4;
    --gold: #b9a583;
    --card-w: 517px;
    --card-h: 295px;
  }
  * { box-sizing: border-box; margin: 0; padding: 0; }
  html, body {
    width: 1200px;
    height: 534px;
    overflow: hidden;
  }
  body {
    background: var(--page-bg);
    font-family: "Saira", sans-serif;
    position: relative;
  }
  .card {
    position: absolute;
    top: 119px;
    width: var(--card-w);
    height: var(--card-h);
    background: var(--card-black);
    overflow: hidden;
    color: var(--text-white);
    --mark: var(--silver);
  }
  .card--left { left: 62px; }
  .card--right { left: 622px; border-radius: 14px; --mark: var(--gold); }

  .card__texture {
    position: absolute;
    inset: 0;
    background:
      radial-gradient(ellipse at 40% 35%, var(--card-shade) 0%, transparent 60%),
      linear-gradient(135deg, #151516 0%, #0b0b0c 55%, #141415 100%);
  }

  .brand {
    position: absolute;
    left: 28px;
    top: 43px;
    width: 205px;
    text-align: center;
    color: var(--mark);
  }
  .brand__circle {
    display: block;
    margin: 0 auto 18px;
  }
  .brand__name {
    display: block;
    font-size: 30px;
    font-weight: 500;
    letter-spacing: 2px;
    line-height: 1;
  }
  .brand__sub {
    display: block;
    font-size: 10px;
    font-weight: 500;
    letter-spacing: 3px;
    margin-top: 5px;
  }

  .details {
    position: absolute;
    left: 246px;
    top: 0;
    right: 8px;
    text-transform: uppercase;
    white-space: nowrap;
    letter-spacing: 0.4px;
  }
  .details > * { position: absolute; left: 0; line-height: 1.1; }
  .details__name { top: 47px; font-size: 13px; font-weight: 600; letter-spacing: 0.8px; }
  .details__company { top: 65px; font-size: 9px; font-weight: 500; }
  .details__address { top: 88px; font-size: 10px; font-weight: 500; }
  .contact { list-style: none; top: 114px; }
  .contact li {
    display: flex;
    align-items: center;
    height: 12.5px;
    font-size: 9px;
    font-weight: 500;
  }
  .contact svg { width: 9px; height: 8px; margin-right: 6px; fill: var(--text-white); flex: none; }
  .details__abn { top: 178px; font-size: 9px; }
  .details__bsa { top: 190px; font-size: 9px; }
  .details__licensed { top: 214px; font-size: 10px; font-weight: 500; }
  .details__services { top: 226px; font-size: 8.6px; font-weight: 500; }
  .details__services span { margin: 0 4px; }
</style>
</head>
<body>

<section class="card card--left">
  <div class="card__texture" role="img" aria-label="Dark mosaic of interlocking cube shapes as background texture"></div>
  <div class="brand">
    <svg class="brand__circle" width="164" height="164" viewBox="0 0 164 164" aria-hidden="true">
      <circle cx="82" cy="82" r="73" fill="none" stroke="currentColor" stroke-width="16"/>
    </svg>
    <span class="brand__name">TORVANE</span>
    <span class="brand__sub">CONSTRUCTION</span>
  </div>
  <div class="details">
    <p class="details__name">Marek Lindqvist</p>
    <p class="details__company">Torvane Construction Pty. Ltd.</p>
    <p class="details__address">PO Box 8640 Dunmore QLD 4170</p>
    <ul class="contact">
      <li><svg viewBox="0 0 10 8"><path d="M1 2h8v1.5H7V3H3v.5H1zM2 4h6l1 4H1z"/></svg>000 000 0000</li>
      <li><svg viewBox="0 0 10 8"><path d="M3 0h4v2H3zM1 2.5h8v4H7.5V5h-5v1.5H1zM2.5 5.5h5V8h-5z"/></svg>000 000 0000</li>
      <li><svg viewBox="0 0 10 8"><path d="M0 1h10v6H0zM1 2l4 3 4-3v-.2H1z"/></svg>person@torvaneconstruction.example.au</li>
      <li><svg viewBox="0 0 10 10"><circle cx="5" cy="5" r="4.5"/></svg>www.torvaneconstruction.example.au</li>
    </ul>
    <p class="details__abn">ABN: 47209836512</p>
    <p class="details__bsa">BSA license: xxx-xxxx</p>
    <p class="details__licensed">Licensed builders specialising in:</p>
    <p class="details__services">Bathrooms<span>|</span>Kitchens<span>|</span>Commercial interiors</p>
  </div>
</section>

<section class="card card--right">
  <div class="card__texture" role="img" aria-label="Dark mosaic of interlocking cube shapes as background texture"></div>
  <div class="brand">
    <svg class="brand__circle" width="164" height="164" viewBox="0 0 164 164" aria-hidden="true">
      <circle cx="82" cy="82" r="73" fill="none" stroke="currentColor" stroke-width="16"/>
    </svg>
    <span class="brand__name">TORVANE</span>
    <span class="brand__sub">CONSTRUCTION</span>
  </div>
  <div class="details">
    <p class="details__name">Marek Lindqvist</p>
    <p class="details__company">Torvane Construction Pty. Ltd.</p>
    <p class="details__address">PO Box 8640 Dunmore QLD 4170</p>
    <ul class="contact">
      <li><svg viewBox="0 0 10 8"><path d="M1 2h8v1.5H7V3H3v.5H1zM2 4h6l1 4H1z"/></svg>000 000 0000</li>
      <li><svg viewBox="0 0 10 8"><path d="M3 0h4v2H3zM1 2.5h8v4H7.5V5h-5v1.5H1zM2.5 5.5h5V8h-5z"/></svg>000 000 0000</li>
      <li><svg viewBox="0 0 10 8"><path d="M0 1h10v6H0zM1 2l4 3 4-3v-.2H1z"/></svg>person@torvaneconstruction.example.au</li>
      <li><svg viewBox="0 0 10 10"><circle cx="5" cy="5" r="4.5"/></svg>www.torvaneconstruction.example.au</li>
    </ul>
    <p class="details__abn">ABN: 47209836512</p>
    <p class="details__bsa">BSA license: xxx-xxxx</p>
    <p class="details__licensed">Licensed builders specialising in:</p>
    <p class="details__services">Bathrooms<span>|</span>Kitchens<span>|</span>Commercial interiors</p>
  </div>
</section>

</body>
</html>
```